Bold Biz Card & Stationary for a Marketing Company
Cobalt Heron Marketing Solutions
Bright & Fun-filled
Linda Hollow
Owner
2417 Maple Ridge Dr
Longmont CO 80503
lindahollow@cobaltheronmarketing.example
cobaltheronmarketing.example
I want something that is unique and/or eye catching.

```html
<!DOCTYPE html>
<html lang="en">
<head>
<meta charset="utf-8">
<title>Cobalt Heron Marketing Solutions – Stationery Set</title>
<link href="https://fonts.googleapis.com/css2?family=Montserrat:wght@400;600&display=swap" rel="stylesheet">
<style>
  :root{
    --orange:#f08a3c;
    --orange-deep:#e4762a;
    --red:#d63a2c;
    --paper:#ffffff;
    --ink:#6b6b6b;
    --backdrop:#3b3431;
  }
  *{box-sizing:border-box;margin:0;padding:0}
  html,body{width:1200px;height:365px;overflow:hidden;background:var(--backdrop)}
  body{position:relative;font-family:"Montserrat",Arial,sans-serif;color:var(--ink)}
  .sheet{position:absolute;background:var(--paper);box-shadow:0 2px 6px rgba(0,0,0,.35);overflow:hidden}
  .brand{display:flex;align-items:center;gap:4px;color:var(--orange-deep);font-weight:600;text-transform:uppercase;line-height:1.15;white-space:nowrap}
  .brand-dot{flex:none;border-radius:50%;background:var(--red)}
  .band{position:absolute;left:0;right:0;bottom:0;background:var(--orange)}
  .contact{position:absolute;font-size:4px;line-height:1.5;color:var(--ink)}
  .contact.on-orange{color:#fff}

  /* business cards */
  .card-front{left:19px;top:112px;width:96px;height:44px}
  .card-front .brand{position:absolute;left:6px;top:7px;font-size:4.2px}
  .card-front .brand-dot{width:7px;height:7px}
  .card-front .contact{left:6px;bottom:5px;font-size:3.4px}
  .card-back{left:19px;top:165px;width:96px;height:44px;background:var(--orange)}
  .card-back .contact{left:6px;top:8px;font-size:3.4px}
  .card-back .contact strong{font-weight:600;font-size:4.2px}

  /* letterhead */
  .letterhead{left:144px;top:30px;width:151px;height:265px}
  .letterhead .brand{position:absolute;left:10px;top:12px;font-size:5.2px}
  .letterhead .brand-dot{width:9px;height:9px}
  .letterhead .band{height:44px}
  .letterhead .contact{left:10px;bottom:12px}

  /* envelope */
  .envelope{left:312px;top:72px;width:204px;height:103px}
  .envelope .brand{position:absolute;left:8px;top:8px;font-size:4.6px}
  .envelope .brand-dot{width:8px;height:8px}
  .envelope .contact{left:8px;top:24px;font-size:3.4px}

  /* note card */
  .notecard{left:312px;top:192px;width:204px;height:108px}
  .notecard .brand{position:absolute;left:10px;top:14px;font-size:4.6px}
  .notecard .brand-dot{width:8px;height:8px}
  .notecard .band{height:44px}
  .notecard .contact{left:10px;top:34px;font-size:3.4px}

  /* presentation folder */
  .folder{left:540px;top:30px;width:624px;height:312px;display:flex}
  .folder-flap{width:312px;height:100%;background:var(--orange);position:relative}
  .folder-flap .contact{left:0;right:0;bottom:10px;text-align:center;font-size:4px}
  .folder-cover{flex:1;position:relative;border-left:1px solid var(--orange-deep)}
  .folder-cover .brand{position:absolute;left:40px;top:76px;font-size:11px;gap:8px}
  .folder-cover .brand-dot{width:22px;height:22px}
  .folder-cover .contact{left:0;right:0;bottom:10px;text-align:center;font-size:4px}
</style>
</head>
<body>

  <section class="sheet card-front" aria-label="Business card front">
    <div class="brand"><span class="brand-dot"></span>Cobalt Heron<br>Marketing Solutions</div>
    <p class="contact">cobaltheronmarketing.example</p>
  </section>

  <section class="sheet card-back" aria-label="Business card back">
    <p class="contact on-orange"><strong>Linda Hollow</strong><br>Owner<br>2417 Maple Ridge Dr<br>Longmont CO 80503<br>lindahollow@cobaltheronmarketing.example</p>
  </section>

  <section class="sheet letterhead" aria-label="Letterhead">
    <div class="brand"><span class="brand-dot"></span>Cobalt Heron<br>Marketing Solutions</div>
    <div class="band"></div>
    <p class="contact on-orange">2417 Maple Ridge Dr<br>Longmont CO 80503<br>cobaltheronmarketing.example</p>
  </section>

  <section class="sheet envelope" aria-label="Envelope">
    <div class="brand"><span class="brand-dot"></span>Cobalt Heron<br>Marketing Solutions</div>
    <p class="contact">2417 Maple Ridge Dr<br>Longmont CO 80503</p>
  </section>

  <section class="sheet notecard" aria-label="Note card">
    <div class="brand"><span class="brand-dot"></span>Cobalt Heron<br>Marketing Solutions</div>
    <p class="contact">cobaltheronmarketing.example</p>
    <div class="band"></div>
  </section>

  <section class="sheet folder" aria-label="Presentation folder">
    <div class="folder-flap">
      <p class="contact on-orange">2417 Maple Ridge Dr · Longmont CO 80503 · cobaltheronmarketing.example</p>
    </div>
    <div class="folder-cover">
      <div class="brand"><span class="brand-dot"></span>Cobalt Heron<br>Marketing Solutions</div>
      <p class="contact">cobaltheronmarketing.example</p>
    </div>
  </section>

</body>
</html>
```